Fern Harbor AG – The secret mission

Hi all. We would love to enhance our website and the sales funnel like on our website www.fernharbor.ch
We are looking for a clean and fresh design which is reflecting our
two main passions: "gaming and investing".
For infos pls have a look at the website www.fernharbor.ch, our youtube channel.
You find many info attached. We are curious how you interprete the topic.

Target Market(s)

Gamers | Investor - worldwide market

Industry/Entity Type

Games

Number of Pages Required

5+ page

Requirements
Must have
• 6 Sites, fresh and modern design (gaming)
Nice to have
• sales funnel (Get involved page) in the same design, webshop
Should not have
• Our shares are on a blockchain, which are very modern (www.velnix.ch). So blockchain design is okay but please no affiliation to bitcoin or crytpocurrencies. thx.

```html
<!DOCTYPE html>
<html lang="en">
<head>
<meta charset="utf-8">
<title>Fern Harbor AG – FinTech in Gaming</title>
<link href="https://fonts.googleapis.com/css2?family=Poppins:wght@400;500;600;700&display=swap" rel="stylesheet">
<style>
:root{
  --red:#e8262d;
  --dark:#1d1e23;
  --ink:#222;
  --muted:#8a8a8a;
  --line:#ececec;
  --hero:#eef0f2;
}
*{box-sizing:border-box;margin:0;padding:0}
html,body{width:1200px;height:3664px;overflow:hidden}
body{font-family:'Poppins',sans-serif;color:var(--ink);background:#fff;position:relative}
.abs{position:absolute}
.topbar{top:0;left:0;width:1200px;height:32px;background:#fff;font-size:10px;color:#666;display:flex;justify-content:flex-end;align-items:center;gap:22px;padding-right:120px;border-bottom:1px solid var(--line)}
.topbar .welcome{background:var(--red);color:#fff;padding:0 14px;line-height:32px}
.brand{top:10px;left:120px;display:flex;align-items:center;gap:8px}
.brand .dot{width:64px;height:64px;border-radius:50%;background:var(--red)}
.brand span{font-weight:700;font-size:14px;color:var(--ink)}
.nav{top:32px;left:0;width:1200px;height:80px;display:flex;justify-content:flex-end;align-items:center;gap:34px;padding-right:120px;font-size:12px;color:#444}
.nav .active{color:var(--red)}
.hero{top:112px;left:0;width:1200px;height:608px;background:linear-gradient(90deg,#fbfbfb,var(--hero))}
.hero-photo{top:112px;left:560px;width:560px;height:608px;background:linear-gradient(135deg,#e3c49a,#c9a16f 45%,#4a6a8e)}
.hero-text{top:245px;left:120px;width:400px}
.eyebrow{color:var(--red);font-size:18px;font-weight:500}
.hero h1{font-size:70px;line-height:1.05;font-weight:600;margin-top:14px}
.hero h1 b{display:block;font-weight:700}
.hero p{font-size:11px;color:#555;margin-top:34px;line-height:1.7}
.btn{display:inline-block;background:var(--red);color:#fff;font-size:10px;font-weight:600;padding:14px 26px;margin-top:30px}
.card{width:220px;height:152px;background:#fff;box-shadow:0 4px 20px rgba(0,0,0,.08);padding:20px 18px}
.card svg{width:40px;height:40px;stroke:var(--red);fill:none;stroke-width:2}
.card h3{font-size:14px;font-weight:600;margin-top:20px}
.card p{font-size:10px;color:var(--muted);margin-top:6px;line-height:1.5}
.mission{top:880px;left:400px;width:400px;text-align:center}
.mission h2{font-size:26px;font-weight:700;line-height:1.2}
.mission h2 small{display:block;font-size:34px}
.mission .mark{width:56px;height:56px;border-radius:50%;background:var(--red);margin:40px auto 0}
.mission p{font-size:11px;color:#666;line-height:1.7;margin-top:36px}
.story-title{top:1500px;left:0;width:1200px;text-align:center;font-size:34px;font-weight:500}
.story-sub{top:1560px;left:360px;width:480px;text-align:center;font-size:11px;color:var(--muted);line-height:1.6}
.story-photo{top:1740px;left:120px;width:470px;height:480px;background:linear-gradient(160deg,#f2f2f2,#dcd6cc 55%,#e0b64a)}
.posts{top:1700px;left:730px;width:380px}
.posts h3{font-size:22px;font-weight:600;margin-bottom:24px}
.post{display:flex;gap:18px;padding:22px 0 22px 20px;border-bottom:1px solid var(--line);font-size:11px;color:#555;line-height:1.6}
.post.first{box-shadow:0 4px 20px rgba(0,0,0,.08);border-right:3px solid var(--red)}
.post svg{flex:none;width:28px;height:28px;stroke:var(--red);fill:none;stroke-width:2}
.more{color:var(--red);font-size:11px;margin:26px 0 0 20px}
.portfolio{top:2240px;left:0;width:1200px;height:260px;background:var(--red);color:#fff}
.portfolio h2{position:absolute;top:62px;left:130px;font-size:44px;font-weight:400}
.portfolio h2 b{font-weight:700}
.portfolio p{position:absolute;top:140px;left:130px;width:260px;font-size:11px;line-height:1.6}
.partner{position:absolute;top:92px;display:flex;align-items:center;gap:12px;font-size:24px;font-weight:600}
.partner i{width:44px;height:44px;background:#fff;display:block;border-radius:50%}
.partner small{display:block;font-size:10px;font-weight:400}
.faq-title{top:2600px;left:0;width:1200px;text-align:center;font-size:34px;font-weight:500}
.faq{left:240px;width:740px}
.faq-item{display:flex;align-items:center;gap:22px;height:64px;padding:0 20px;background:#fff;box-shadow:0 3px 16px rgba(0,0,0,.08);font-size:14px;font-weight:600;margin-bottom:26px}
.faq-item .plus{width:26px;height:26px;border-radius:50%;background:var(--red);color:#fff;display:flex;align-items:center;justify-content:center;font-size:16px;font-weight:400}
.faq-item.open .plus{background:#111}
.faq-answer{font-size:11px;color:#666;line-height:1.7;padding:0 20px 26px 68px;margin-top:-16px}
.footer{top:3320px;left:0;width:1200px;height:344px;background:var(--dark);color:#cfd0d4}
.f-brand{position:absolute;top:40px;left:120px;text-align:center;width:150px}
.f-brand .dot{width:60px;height:60px;border-radius:50%;background:#fff;margin:0 auto}
.f-brand b{display:block;color:#fff;font-size:14px;margin-top:10px}
.f-brand p{font-size:10px;margin-top:14px}
.social{display:flex;gap:10px;justify-content:center;margin-top:12px}
.social i{width:22px;height:22px;border-radius:50%;background:#fff;display:block}
.f-col{position:absolute;top:40px;font-size:10px;line-height:2.1}
.f-col h4{color:#fff;font-size:15px;font-weight:600;margin-bottom:12px}
.f-col .row{display:flex;gap:10px;align-items:flex-start}
.f-col svg{width:12px;height:12px;margin-top:6px;stroke:var(--red);fill:none;stroke-width:2;flex:none}
</style>
</head>
<body>
<div class="abs topbar"><span class="welcome">Welcome to FinTech in Gaming</span><span>Company Reg: CHE-100.200.300</span><span>info@fernharbor.ch</span></div>
<div class="abs brand"><div class="dot"></div><span>Fern Harbor AG</span></div>
<nav class="abs nav"><span class="active">Home</span><span>About Us</span><span>Get Involved</span><span>Frequently Asked Questions</span><span>Press</span><span>Contact Us</span></nav>

<section class="abs hero"></section>
<div class="abs hero-photo" role="img" aria-label="Two young gamers playing on a handheld device"></div>
<div class="abs hero hero-text" style="height:auto;background:none">
  <div class="eyebrow">Made in Switzerland</div>
  <h1>FinTech in<b>Gaming</b></h1>
  <p>We are an investment holding with the purpose to invest in FinTech in gaming to enhance the gaming experience.</p>
  <span class="btn">CONTACT US</span>
</div>

<div class="abs card" style="top:830px;left:130px"><svg viewBox="0 0 40 40"><rect x="4" y="12" width="32" height="18" rx="8"/><path d="M12 17v6M9 20h6"/><circle cx="27" cy="19" r="1.5"/><circle cx="30" cy="23" r="1.5"/></svg><h3>Gaming Experience</h3><p>We turn our passion for play<br>into real value.</p></div>
<div class="abs card" style="top:1100px;left:130px"><svg viewBox="0 0 40 40"><circle cx="17" cy="17" r="12"/><path d="M17 10v14M21 13h-5a3 3 0 000 6h2a3 3 0 010 6h-5"/><circle cx="27" cy="27" r="9"/></svg><h3>Capital Increase</h3><p>We grow our portfolio<br>step by step.</p></div>
<div class="abs card" style="top:830px;left:840px"><svg viewBox="0 0 40 40"><path d="M8 24v-4a12 12 0 0124 0v4"/><rect x="5" y="22" width="7" height="11" rx="2"/><rect x="28" y="22" width="7" height="11" rx="2"/></svg><h3>Investive Platform</h3><p>We open gaming to new<br>kinds of investors.</p></div>
<div class="abs card" style="top:1100px;left:840px"><svg viewBox="0 0 40 40"><rect x="4" y="6" width="32" height="22" rx="2"/><path d="M14 34h12M20 28v6"/></svg><h3>Digital Assembly</h3><p>We hold our meetings<br>fully online.</p></div>

<div class="abs mission">
  <h2>Fern Harbor AG<small>The secret mission</small></h2>
  <div class="mark"></div>
  <p>We are an investment holding with the purpose to invest in FinTech in gaming to enhance the gaming experience and to build the basis to unite the gamers to enjoy their games.</p>
</div>

<h2 class="abs story-title">Whats the story with the name “Fern Harbor”?</h2>
<p class="abs story-sub">One of the first online games was called Harbor – a “hidden” game level that was an enormous success, launched in the mid 1990s.</p>
<div class="abs story-photo" role="img" aria-label="Smiling businessman with tablet beside stacks of gold coins and a rising red arrow"></div>
<div class="abs posts">
  <h3>Recent Posts</h3>
  <div class="post first"><svg viewBox="0 0 28 28"><rect x="3" y="6" width="16" height="19"/><path d="M8 3h16v19"/></svg><span>The history and the team behind PLAYVA: interview with founders, part 1</span></div>
  <div class="post"><svg viewBox="0 0 28 28"><rect x="3" y="6" width="16" height="19"/><path d="M8 3h16v19"/></svg><span>The gaming market is ready to broaden – but how can it be done?</span></div>
  <div class="post"><svg viewBox="0 0 28 28"><rect x="3" y="6" width="16" height="19"/><path d="M8 3h16v19"/></svg><span>Why the gaming market needs a broker: a trader’s view on trading preferences</span></div>
  <div class="more">View More</div>
</div>

<section class="abs portfolio">
  <h2>Our <b>Portfolio</b></h2>
  <p>We are proud of each partner we have chosen for our shares.</p>
  <div class="partner" style="left:600px"><i></i><div>PLAYVA<small>www.playva.ch</small></div></div>
  <div class="partner" style="left:860px"><i></i><div>Ledgerline advisory<small>www.ledgerline.ch</small></div></div>
</section>

<h2 class="abs faq-title">Frequently Asked Questions</h2>
<div class="abs faq" style="top:2720px">
  <div class="faq-item"><span class="plus">+</span>What are tokenised shares?</div>
  <div class="faq-item open"><span class="plus">−</span>What is the link between PLAYVA?</div>
  <p class="faq-answer">We are an investment holding with the purpose to invest in FinTech in gaming to enhance the gaming experience and to build the basis to unite the gamers to enjoy their games.</p>
  <div class="faq-item"><span class="plus">+</span>What is PLAYVA?</div>
  <div class="faq-item"><span class="plus">+</span>What is Fern Harbor AG</div>
  <div class="faq-item"><span class="plus">+</span>What are tokenised shares?</div>
</div>

<footer class="abs footer">
  <div class="f-brand"><div class="dot"></div><b>Fern Harbor</b><p>Copyright © 2024 Fern Harbor AG</p><div class="social"><i></i><i></i></div></div>
  <div class="f-col" style="left:460px"><h4>Contact Us</h4>
    <div class="row"><svg viewBox="0 0 12 12"><path d="M6 11s4-4 4-6.5a4 4 0 00-8 0C2 7 6 11 6 11z"/></svg><span>Fern Harbor AG<br>Company Reg: CHE-100.200.300<br>Lindenweg 12 | 4000 Basel | Switzerland</span></div>
    <div class="row"><svg viewBox="0 0 12 12"><rect x="1" y="2.5" width="10" height="7"/><path d="M1 3l5 4 5-4"/></svg><span>info@fernharbor.ch</span></div>
    <div class="row"><svg viewBox="0 0 12 12"><circle cx="6" cy="6" r="5"/><path d="M1 6h10M6 1c2 2 2 8 0 10M6 1c-2 2-2 8 0 10"/></svg><span>www.fernharbor.ch</span></div>
  </div>
  <div class="f-col" style="left:900px"><h4>Pages</h4>Home<br>About Us<br>Get Involved<br>Frequently Asked Questions<br>Press<br>Contact Us</div>
</footer>
</body>
</html>
```